Ember needs a new design we have an updated logo and want a high qualitative high end feel

feel and aesthetic should be high qualitative like the packaging in a zelvo or the qualatative weight/feel of an zelvo design. modern, elegant bold.probably just the ember logo on the backone vesion could be blue background white letter ... open to ideas
legal, insurance , medical, finance vantor 300
Information Technology
Serif

```html
<!DOCTYPE html>
<html lang="en">
<head>
<meta charset="utf-8">
<title>Ember Business Card</title>
<link href="https://fonts.googleapis.com/css2?family=Roboto:wght@400;500&display=swap" rel="stylesheet">
<style>
  :root {
    --navy: #243447;
    --navy-light: #2c3e52;
    --white: #ffffff;
    --grey-text: #7d7d7d;
    --grey-band: #a9a9a9;
    --backdrop: #3a3a3a;
    --divider: #cfcfcf;
  }
  * { margin: 0; padding: 0; box-sizing: border-box; }
  html, body {
    width: 1200px; height: 800px; overflow: hidden;
    background: var(--backdrop);
    font-family: "Roboto", sans-serif;
  }
  .canvas { position: relative; width: 1200px; height: 800px; }
  .card {
    position: absolute; width: 522px; height: 302px;
    box-shadow: 0 6px 14px rgba(0,0,0,.45);
    overflow: hidden;
  }
  .card-front {
    left: 357px; top: 92px;
    background: radial-gradient(ellipse at 50% 45%, var(--navy-light), var(--navy) 70%);
    color: var(--white);
  }
  .card-back { left: 359px; top: 427px; background: var(--white); }

  .wordmark {
    position: absolute; display: flex; align-items: center; gap: 8px;
    font-weight: 400; letter-spacing: 1px; line-height: 1;
  }
  .wordmark-dot { width: 7px; height: 7px; border-radius: 50%; background: currentColor; align-self: flex-start; }
  .card-front .wordmark { left: 0; right: 0; top: 150px; justify-content: center; font-size: 64px; }
  .card-back .wordmark { left: 40px; top: 138px; font-size: 50px; color: var(--navy); }

  .front-url {
    position: absolute; left: 0; right: 0; bottom: 22px;
    text-align: center; font-size: 13.5px; letter-spacing: .3px;
  }

  .divider { position: absolute; left: 272px; top: 83px; width: 1px; height: 130px; background: var(--divider); }

  .contact { position: absolute; left: 296px; top: 78px; color: var(--grey-text); }
  .contact-name { font-size: 19px; font-weight: 500; color: var(--navy); line-height: 1.1; }
  .contact-role { font-size: 12.5px; margin-top: 3px; }
  .contact-address { font-size: 13.5px; line-height: 18px; margin-top: 17px; }
  .contact-lines { margin-top: 14px; font-size: 14px; line-height: 18px; }
  .contact-line { display: flex; align-items: center; gap: 8px; }
  .contact-line svg { width: 12px; height: 12px; fill: var(--navy); flex: none; }

  .footer-band { position: absolute; left: 0; bottom: 0; width: 522px; height: 14px; }
</style>
</head>
<body>
<main class="canvas">
  <section class="card card-front" aria-label="Card front">
    <div class="wordmark"><span>ember</span><span class="wordmark-dot"></span></div>
    <p class="front-url">www.embergroup.com</p>
  </section>

  <section class="card card-back" aria-label="Card back">
    <div class="wordmark"><span>ember</span><span class="wordmark-dot"></span></div>
    <div class="divider"></div>
    <div class="contact">
      <p class="contact-name">Daniel Hart</p>
      <p class="contact-role">Founder</p>
      <p class="contact-address">Harlow 58 Suite 410<br>City Country KD527</p>
      <div class="contact-lines">
        <p class="contact-line">
          <svg viewBox="0 0 24 24" aria-hidden="true"><path d="M6.6 10.8a15.1 15.1 0 0 0 6.6 6.6l2.2-2.2a1 1 0 0 1 1-.25 11.4 11.4 0 0 0 3.6.57 1 1 0 0 1 1 1V20a1 1 0 0 1-1 1A17 17 0 0 1 3 4a1 1 0 0 1 1-1h3.5a1 1 0 0 1 1 1c0 1.25.2 2.45.57 3.57a1 1 0 0 1-.25 1z"/></svg>
          <span>0184 3307 619</span>
        </p>
        <p class="contact-line">
          <svg viewBox="0 0 24 24" aria-hidden="true"><path d="M2 5h20v14H2zm2 2v.5l8 5 8-5V7zm0 2.8V17h16V9.8l-8 5z"/></svg>
          <span>info@embergroup.com</span>
        </p>
      </div>
    </div>
    <svg class="footer-band" viewBox="0 0 522 14" preserveAspectRatio="none" aria-hidden="true">
      <rect x="0" y="2" width="270" height="12" fill="var(--grey-band)"/>
      <path d="M262 14 C266 4 272 0 282 0 H522 V14 Z" fill="var(--white)"/>
      <path d="M266 14 C270 5 276 1 286 1 H522 V14 Z" fill="var(--navy)"/>
    </svg>
  </section>
</main>
</body>
</html>
```